Business Card Design Project

I want a design for my business cards based on an excisting logo design.

Target Market(s)

Marketeers, PR-peeps, CEO's, decisionmakers, entrepreneurs

Industry/Entity Type

Business

Requirements
Nice to have
• Some visual interest on the back too
Should not have
• Sarif on the font

```html
<!DOCTYPE html>
<html lang="nl">
<head>
<meta charset="utf-8">
<title>LeafLine PR – business cards</title>
<link rel="stylesheet" href="https://fonts.googleapis.com/css2?family=Open+Sans:wght@400;600;700&family=Cinzel:wght@600&display=swap">
<style>
  :root {
    --backdrop: #2c3030;
    --card: #ffffff;
    --grey-brand: #808285;
    --ink: #3a3a3a;
    --green-dark: #0c9a4a;
    --green-light: #a6ce39;
  }
  * { margin: 0; padding: 0; box-sizing: border-box; }
  html, body { width: 971px; height: 1200px; overflow: hidden; }
  body {
    background: var(--backdrop);
    font-family: "Open Sans", Arial, sans-serif;
    position: relative;
  }
  .card {
    position: absolute;
    width: 800px;
    height: 456px;
    background: var(--card);
    border-radius: 28px;
    overflow: hidden;
  }
  .card--front { left: 77px; top: 104px; }
  .card--back { left: 80px; top: 634px; }

  .brand {
    position: absolute;
    display: flex;
    align-items: center;
    color: var(--grey-brand);
    font-weight: 400;
    white-space: nowrap;
  }
  .brand__dot { border-radius: 50%; background: var(--green-light); flex: none; }
  .card--front .brand { left: 45px; top: 44px; font-size: 66px; gap: 40px; }
  .card--front .brand__dot { width: 116px; height: 116px; }

  .holder {
    position: absolute; left: 0; width: 100%; top: 238px;
    text-align: center; font-weight: 700; font-size: 23px; color: var(--ink);
  }
  .contact {
    position: absolute; left: 0; width: 100%; top: 287px;
    text-align: center; font-size: 18px; line-height: 27px; color: var(--ink);
  }
  .contact b { font-style: italic; font-weight: 700; }
  .contact .sep { padding: 0 6px; }

  .swoosh { position: absolute; left: 0; top: 0; width: 800px; height: 456px; }
  .address {
    position: absolute; left: 310px; width: 390px; top: 380px;
    text-align: center; color: #fff; font-size: 21px; line-height: 32px;
  }

  .tagline {
    position: absolute; left: 0; width: 100%; top: 18px;
    text-align: center; font-family: "Cinzel", "Times New Roman", serif;
    font-weight: 600; font-size: 17px; line-height: 24px; color: #4a4a4a;
  }
  .card--back .brand {
    left: 0; width: 100%; top: 90px;
    flex-direction: column; gap: 36px; font-size: 40px;
  }
  .card--back .brand__dot { width: 180px; height: 180px; }
  .web {
    position: absolute; left: 0; width: 100%; top: 400px;
    text-align: center; font-size: 28px; color: var(--ink);
  }
</style>
</head>
<body>
  <section class="card card--front">
    <div class="brand"><span class="brand__dot"></span><span class="brand__name">LeafLine PR</span></div>
    <p class="holder">Mara Jensen</p>
    <p class="contact">
      <b>p</b> : +31(0)6 20481357<span class="sep">|</span><b>e</b> : mara.jensen@leaflinepr.nl<span class="sep">|</span><b>w</b> : www.leaflinepr.nl<br>
      <b>t</b> : social.example/_leaflinepr<span class="sep">|</span><b>f</b> : social.example/leaflinepr
    </p>
    <svg class="swoosh" viewBox="0 0 800 456" aria-hidden="true">
      <path d="M0 400 L412 357 C300 370 150 400 0 426 Z" fill="var(--green-light)"/>
      <path d="M0 448 C150 405 290 368 420 358 C600 348 760 378 800 410 L800 456 L0 456 Z" fill="var(--green-dark)"/>
    </svg>
    <p class="address">Veldstraat 12<br>6702 AB Wageningen</p>
  </section>

  <section class="card card--back">
    <p class="tagline">Systemisch en strategisch PR-<br>Marketing- en communicatieadvies</p>
    <div class="brand"><span class="brand__dot"></span><span class="brand__name">LeafLine PR</span></div>
    <p class="web">www.leaflinepr.nl</p>
  </section>
</body>
</html>
```